Casa Vero Inspections Business Card

I need a business card for my new company. The company is going to provide home inspections. The name of the company is Casa Vero Inspections. I am not sure if I want a single sided card or a double. I have a logo already that I want to incorporate into the card design. I was wondering if I should incorporate a catch phrase on my card or not. If I did the phrase would be "The Intelligent Choice for Home Inspections" but i am unsure how or if to use it on a card. The following information needs to be on the card.
Home Inspection
My Name: Marcus T. Wolford Phone Number: 555-301-7762 Email: mwolford@casaveroinspections.com Website: www.casaveroinspections.com NY HI License # 27300519462

```html
<!DOCTYPE html>
<html lang="en">
<head>
<meta charset="utf-8">
<title>Casa Vero Inspections – Business Card</title>
<link rel="stylesheet" href="https://fonts.googleapis.com/css2?family=Montserrat:wght@500;600;700&display=swap">
<style>
  :root {
    --brand-blue: #146ca9;
    --sky-blue: #75c5ee;
    --card-white: #ffffff;
    --backdrop-dark: #b5b6ba;
    --backdrop-light: #c4c5c7;
  }
  * { margin: 0; padding: 0; box-sizing: border-box; }
  html, body {
    width: 1200px; height: 1200px; overflow: hidden;
    font-family: "Montserrat", sans-serif;
    background: var(--backdrop-dark);
  }
  .backdrop { position: absolute; inset: 0; width: 1200px; height: 1200px; }
  .card {
    position: absolute; left: 199px; width: 802px; height: 459px;
    background: var(--card-white); overflow: hidden;
  }
  .card--front { top: 109px; }
  .card--back { top: 632px; }

  .wordmark {
    position: absolute; display: flex; align-items: center; justify-content: center;
    gap: 14px; color: var(--brand-blue); font-weight: 700; text-align: center;
    text-transform: uppercase; line-height: 1.1;
  }
  .wordmark__square { flex: none; background: var(--brand-blue); }
  .card--front .wordmark { left: 179px; top: 60px; width: 444px; height: 250px; font-size: 44px; }
  .card--front .wordmark__square { width: 28px; height: 28px; }
  .card--back .wordmark { left: 40px; top: 140px; width: 300px; height: 180px; font-size: 30px; gap: 10px; }
  .card--back .wordmark__square { width: 18px; height: 18px; }

  .tagline-band {
    position: absolute; left: 0; top: 366px; width: 100%; height: 44px;
    background: var(--brand-blue); color: var(--card-white);
    display: flex; align-items: center; justify-content: center;
    font-size: 22px; font-weight: 500; letter-spacing: 0.6px;
  }

  .divider {
    position: absolute; left: 350px; top: 90px; width: 2px; height: 278px;
    background: var(--sky-blue);
  }
  .contact {
    position: absolute; left: 380px; top: 128px; width: 395px;
    color: var(--brand-blue); white-space: nowrap;
  }
  .contact__name {
    font-size: 33px; font-weight: 700; letter-spacing: 0.2px;
    line-height: 1; margin-bottom: 26px;
  }
  .contact__list { list-style: none; }
  .contact__item {
    display: flex; align-items: center; gap: 14px;
    font-size: 18px; font-weight: 500; height: 42px; letter-spacing: 0.2px;
  }
  .contact__icon { width: 18px; height: 18px; flex: none; }
  .contact__license {
    font-size: 18px; font-weight: 500; letter-spacing: 0.2px;
    line-height: 24px; margin-top: 7px;
  }
</style>
</head>
<body>
  <svg class="backdrop" viewBox="0 0 1200 1200" aria-hidden="true">
    <rect width="1200" height="1200" fill="var(--backdrop-dark)"/>
    <polygon points="0,0 1200,1200 0,1200" fill="var(--backdrop-light)"/>
  </svg>

  <section class="card card--front">
    <div class="wordmark">
      <span class="wordmark__square"></span>
      <span>Casa Vero<br>Inspections</span>
    </div>
    <div class="tagline-band">The Intelligent Choice for Home Inspections</div>
  </section>

  <section class="card card--back">
    <div class="wordmark">
      <span class="wordmark__square"></span>
      <span>Casa Vero<br>Inspections</span>
    </div>
    <div class="divider"></div>
    <div class="contact">
      <h1 class="contact__name">MARCUS T. WOLFORD</h1>
      <ul class="contact__list">
        <li class="contact__item">
          <svg class="contact__icon" viewBox="0 0 24 24" aria-label="Phone"><path fill="var(--sky-blue)" d="M6.6 10.8a15.1 15.1 0 0 0 6.6 6.6l2.2-2.2c.3-.3.7-.4 1-.2 1.1.4 2.3.6 3.6.6.6 0 1 .4 1 1V20c0 .6-.4 1-1 1A17 17 0 0 1 3 4c0-.6.4-1 1-1h3.5c.6 0 1 .4 1 1 0 1.3.2 2.5.6 3.6.1.3 0 .7-.2 1z"/></svg>
          <span>555-301-7762</span>
        </li>
        <li class="contact__item">
          <svg class="contact__icon" viewBox="0 0 24 24" aria-label="Email"><rect x="2" y="5" width="20" height="14" fill="var(--sky-blue)"/><path d="M2 5l10 8 10-8M2 19l7.5-7M22 19l-7.5-7" stroke="#fff" stroke-width="1.4" fill="none"/></svg>
          <span>mwolford@casaveroinspections.com</span>
        </li>
        <li class="contact__item">
          <svg class="contact__icon" viewBox="0 0 24 24" aria-label="Website"><g fill="none" stroke="var(--sky-blue)" stroke-width="1.8"><circle cx="12" cy="12" r="9.5"/><ellipse cx="12" cy="12" rx="4" ry="9.5"/><path d="M2.5 12h19M4 7h16M4 17h16"/></g></svg>
          <span>www.casaveroinspections.com</span>
        </li>
      </ul>
      <p class="contact__license">NY HI License # 27300519462</p>
    </div>
  </section>
</body>
</html>
```